Business Card Design - Ember Hill Lodge

We are looking at a new design for our business cards that has a modern and professional look. We run a residential aged care facility focussing on the care of residents. The cards will be used for potential clients, consultants and business opportunities in this sector. Blue and white is our main colours and would to see these colours incorporated in the design.
Industry/Entity Type
Business
Contact Information for Business Card
Ember Hill Lodge, Dean Marsh, dmarsh@emberhilllodge-mail.example, Finance Manager, 0491 372 608, BCom, 27 Marbury Way, Carrowbrook, Qld 4511.
Look and feel

```html
<!DOCTYPE html>
<html lang="en">
<head>
<meta charset="utf-8">
<title>Ember Hill Lodge – Business Card</title>
<link href="https://fonts.googleapis.com/css2?family=Raleway:ital,wght@0,400;0,500;0,700;1,400&display=swap" rel="stylesheet">
<style>
  :root {
    --page: #ffffff;
    --frame: #333333;
    --card: #dce3ea;
    --ink: #4b5e6e;
    --brand: #557e99;
    --ornament-a: #c3ced8;
    --ornament-b: #d3dce4;
    --bar-start: #00aeef;
    --bar-end: #2b4e7a;
  }
  html, body {
    margin: 0;
    padding: 0;
    width: 1200px;
    height: 1200px;
    overflow: hidden;
    background: var(--page);
    font-family: "Raleway", sans-serif;
  }
  .sheet { position: relative; width: 1200px; height: 1200px; }
  .card-frame {
    position: absolute;
    left: 168px;
    width: 860px;
    border: 3px solid var(--frame);
    background: var(--page);
  }
  .card-frame--front { top: 57px; height: 516px; }
  .card-frame--back { top: 617px; height: 520px; }
  .card {
    position: absolute;
    left: 19px;
    top: 20px;
    width: 820px;
    background: var(--card);
    overflow: hidden;
  }
  .card-frame--front .card { height: 478px; }
  .card-frame--back .card { height: 476px; }

  .ornament {
    position: absolute;
    background: linear-gradient(135deg, var(--ornament-b), var(--ornament-a));
    opacity: 0.55;
  }
  .ornament--front { left: 386px; top: 12px; width: 434px; height: 196px; border-radius: 60% 0 0 40%; }
  .ornament--back-left { left: 0; top: 0; width: 114px; height: 326px; border-radius: 0 50% 60% 0; }
  .ornament--back-right { right: 0; bottom: 0; width: 94px; height: 374px; border-radius: 60% 0 0 0; }

  .brand-name {
    position: absolute;
    color: var(--brand);
    font-weight: 500;
    white-space: nowrap;
    margin: 0;
    display: flex;
    align-items: center;
    gap: 12px;
  }
  .brand-name .brand-dot {
    display: inline-block;
    border-radius: 50%;
    background: var(--brand);
  }
  .brand-name--front { left: 66px; top: 100px; font-size: 27px; }
  .brand-name--front .brand-dot { width: 22px; height: 22px; }
  .brand-name--back { left: 0; right: 0; top: 208px; justify-content: center; font-size: 46px; }
  .brand-name--back .brand-dot { width: 36px; height: 36px; }

  .rule {
    position: absolute;
    left: 0;
    top: 248px;
    width: 442px;
    height: 4px;
    background: var(--brand);
  }
  .holder {
    position: absolute;
    right: 18px;
    top: 216px;
    text-align: right;
  }
  .holder-name {
    margin: 0;
    font-size: 60px;
    font-weight: 700;
    color: var(--brand);
    line-height: 66px;
    white-space: nowrap;
  }
  .holder-title {
    margin: 4px 6px 0 0;
    font-size: 22px;
    font-style: italic;
    color: var(--brand);
  }
  .contact {
    position: absolute;
    left: 18px;
    top: 312px;
    margin: 0;
    font-size: 26px;
    color: var(--ink);
    line-height: 31px;
    font-style: normal;
  }
  .contact-line { display: flex; align-items: center; gap: 8px; white-space: nowrap; }
  .contact-icon { width: 30px; height: 24px; fill: var(--ink); flex: none; }
  .bar {
    position: absolute;
    left: 0;
    bottom: 0;
    width: 820px;
    height: 24px;
    background: linear-gradient(90deg, var(--bar-start), var(--bar-end));
  }
</style>
</head>
<body>
<main class="sheet">
  <section class="card-frame card-frame--front" aria-label="Business card front">
    <div class="card">
      <div class="ornament ornament--front" role="img" aria-label="Faint floral swirl ornament with leaves"></div>
      <p class="brand-name brand-name--front"><span class="brand-dot"></span>Ember Hill Lodge</p>
      <div class="rule"></div>
      <div class="holder">
        <h1 class="holder-name">Dean Marsh</h1>
        <p class="holder-title">Finance Manager</p>
      </div>
      <address class="contact">
        <div class="contact-line">Ember Hill Lodge,</div>
        <div class="contact-line">Bcom, 27 Marbury Way, Carrowbrook, Qld 4511.</div>
        <div class="contact-line">
          <svg class="contact-icon" viewBox="0 0 30 24" aria-hidden="true">
            <path d="M2 8 C2 2 28 2 28 8 L28 10 L22 10 L22 7 C18 5 12 5 8 7 L8 10 L2 10 Z"/>
            <path d="M8 11 L22 11 L26 22 L4 22 Z"/>
          </svg>
          <span>0491 372 608</span>
        </div>
        <div class="contact-line">
          <svg class="contact-icon" viewBox="0 0 30 24" aria-hidden="true">
            <path d="M2 3 H28 V21 H2 Z M5 6 V18 H25 V6 L15 14 Z" fill-rule="evenodd"/>
          </svg>
          <span>dmarsh@emberhilllodge-mail.example</span>
        </div>
      </address>
      <div class="bar"></div>
    </div>
  </section>

  <section class="card-frame card-frame--back" aria-label="Business card back">
    <div class="card">
      <div class="ornament ornament--back-left" role="img" aria-label="Faint floral vine ornament along the left edge"></div>
      <div class="ornament ornament--back-right" role="img" aria-label="Faint floral vine ornament along the right edge"></div>
      <p class="brand-name brand-name--back"><span class="brand-dot"></span>Ember Hill Lodge</p>
    </div>
  </section>
</main>
</body>
</html>
```